Flyer for Compassion training days

I need a A5-size, single-sided flyer design for my training days. They are weekends in a blend of Compassionate Communication and Buddhist teachings called Palomere Communication. The logo for Palomere that should be included.
The flyer needs room for 1) course title, 2) course dates, location & price, 3) course description, 4) booking info, 5) my picture & short bio, and 6) the palomere.co website (yes, it is 'co' and not 'com).
Updates

Target Market(s)

Women 35-65 years, well-educated, spiritually minded. May have interests like yoga and meditation.

Industry/Entity Type

Health And Wellness

Font styles to use
Sans Serif
Other font styles liked:
• Blue Plaque, Josefina are both great

Colors
fbf289
fdf9cf
cfeae6
33b8a4

Requirements
Must have
• The Palomere logo; my picture.
• Elegance. Calm and expansive feel.
• The poster provided in the project files shows you the kind of information I need to include.
• Colours -- greens and yellows, but the options on pixel harbor are not quite the right shades.
• The logo colour can be changed.
Nice to have
• Classy (but not cliche) image associated with Buddhism; gentle curves similar to those on the business card (see project files).
Should not have
• Dark background. Busy, loud design. Overly 'swirly' design. Images that I have to buy separately.

```html
<!DOCTYPE html>
<html lang="en">
<head>
<meta charset="utf-8">
<title>Palomere Communication – Core Course Flyer</title>
<link rel="stylesheet" href="https://fonts.googleapis.com/css2?family=Josefin+Sans:ital,wght@0,400;0,600;0,700;1,700&display=swap">
<style>
  :root {
    --green: #3fb34a;
    --green-deep: #2e9e3e;
    --lime: #8cc63f;
    --yellow: #e6e82a;
    --ink: #3a3a3a;
    --ink-soft: #555;
    --page: #eceeed;
    --mist: #efe7e6;
  }
  * { margin: 0; padding: 0; box-sizing: border-box; }
  html, body { width: 1200px; height: 1000px; overflow: hidden; background: var(--page); }
  body { font-family: "Josefin Sans", sans-serif; color: var(--ink); }

  .flyer {
    position: absolute; left: 30px; top: 98px;
    width: 1140px; height: 803px; overflow: hidden;
    background: linear-gradient(135deg, #f4ecec 0%, var(--mist) 45%, #f1efe9 100%);
    box-shadow: 0 4px 18px rgba(0,0,0,.12);
  }
  .flyer-art { position: absolute; inset: 0; width: 1140px; height: 803px; }

  .title-block { position: absolute; left: 100px; width: 540px; text-align: center; white-space: nowrap; }
  .title-formula { top: 222px; font-weight: 700; font-size: 20px; line-height: 32px; letter-spacing: .3px; }
  .title-formula .plus { color: var(--green); }
  .title-name {
    top: 286px; font-weight: 700; font-size: 74px; line-height: 80px; letter-spacing: 1px;
    background: linear-gradient(90deg, var(--green) 0%, var(--green) 38%, var(--yellow) 60%, var(--green) 84%);
    -webkit-background-clip: text; background-clip: text; color: transparent;
  }
  .title-sub { top: 378px; font-weight: 600; font-size: 46px; line-height: 50px; color: var(--green); letter-spacing: .5px; }

  .course-block { position: absolute; left: 253px; width: 260px; text-align: center; }
  .course-label { top: 446px; font-size: 15px; line-height: 18px; }
  .course-dates {
    position: absolute; left: 343px; top: 474px; width: 80px; height: 62px;
    background: linear-gradient(135deg, var(--yellow), var(--lime));
    color: var(--green-deep); font-weight: 700; font-size: 21px; line-height: 23px;
    text-align: center; padding-top: 9px;
  }
  .course-venue { top: 554px; color: var(--green); font-weight: 700; font-size: 18px; line-height: 23px; }
  .course-rule { position: absolute; left: 310px; width: 146px; top: 604px; border-top: 1px solid var(--ink); }
  .course-price { top: 612px; font-size: 15px; line-height: 18px; }

  .course-info {
    position: absolute; left: 739px; top: 40px; width: 390px;
    font-size: 15px; line-height: 21.7px; color: var(--ink-soft);
  }
  .course-info strong { color: var(--ink); font-weight: 700; }
  .course-info p + p, .course-info ul + p { margin-top: 21.7px; }
  .course-info ul { list-style: none; margin-left: 12px; }
  .course-info li::before { content: "* "; }
  .course-info li .wrap { display: block; padding-left: 11px; }

  .booking { position: absolute; right: 37px; top: 536px; text-align: right; }
  .booking-main { font-weight: 700; font-size: 20px; line-height: 24px; color: var(--ink); }
  .booking-alt { font-size: 16px; line-height: 20px; margin-top: 4px; }
  .booking-alt strong { font-weight: 700; }

  .facilitator { position: absolute; right: 312px; top: 650px; width: 420px; text-align: right; }
  .facilitator-label { color: var(--green); font-size: 13px; line-height: 15px; text-decoration: underline; letter-spacing: .3px; }
  .facilitator-name { color: var(--green-deep); font-weight: 700; font-size: 21px; line-height: 24px; margin-top: 3px; }
  .facilitator-bio { font-size: 14px; line-height: 20px; margin-top: 4px; color: var(--ink-soft); }

  .brand-mark { position: absolute; left: 905px; top: 670px; display: flex; align-items: center; gap: 10px; }
  .brand-mark .dot { width: 22px; height: 22px; border-radius: 50%; background: var(--green); }
  .brand-mark .name { font-weight: 700; font-size: 30px; line-height: 34px; color: var(--green); }
  .site-url { position: absolute; right: 29px; top: 752px; font-weight: 700; font-style: italic; font-size: 30px; line-height: 34px; color: var(--green); }
</style>
</head>
<body>
<main class="flyer">
  <svg class="flyer-art" viewBox="0 0 1140 803">
    <defs>
      <linearGradient id="heartStroke" x1="0" y1="0" x2="1" y2="1">
        <stop offset="0" stop-color="#3fb34a"/>
        <stop offset=".6" stop-color="#8cc63f"/>
        <stop offset="1" stop-color="#3fb34a"/>
      </linearGradient>
      <linearGradient id="bandFill" x1="0" y1="0" x2="1" y2="0">
        <stop offset="0" stop-color="#7cc242"/>
        <stop offset=".5" stop-color="#c6e04a"/>
        <stop offset="1" stop-color="#eef02e"/>
      </linearGradient>
      <linearGradient id="waterFill" x1="0" y1="0" x2="1" y2="1">
        <stop offset="0" stop-color="#dfe9ee"/>
        <stop offset=".5" stop-color="#9cc9dd"/>
        <stop offset="1" stop-color="#eef1f2"/>
      </linearGradient>
      <radialGradient id="portraitFill" cx=".5" cy=".45" r=".6">
        <stop offset="0" stop-color="#c7ab7f"/>
        <stop offset="1" stop-color="#6e5436"/>
      </radialGradient>
      <clipPath id="portraitClip">
        <path d="M589 476 C565 425 490 425 485 485 C482 550 550 610 612 673 C670 610 725 540 712 475 C700 420 615 425 589 476 Z"/>
      </clipPath>
    </defs>

    <rect class="scene-water" x="0" y="312" width="363" height="491" fill="url(#waterFill)" role="img" aria-label="Photo of white lotus flowers floating on calm blue water"/>

    <path class="white-base" d="M430 803 C520 700 640 650 760 625 C900 600 1050 620 1140 600 L1140 803 Z" fill="#fff"/>
    <path class="accent-band" d="M716 520 C800 470 900 500 1000 500 C1080 500 1120 490 1140 480 L1140 600 C1060 640 950 650 850 640 C790 630 750 600 716 520 Z" fill="url(#bandFill)"/>
    <path class="green-swoosh" d="M370 716 C420 755 455 780 475 803 L545 803 C505 768 445 738 370 716 Z" fill="#5dbb46"/>

    <path class="title-heart" d="M329 140 C300 60 180 30 90 80 C10 130 5 260 60 380 C120 510 260 610 370 716 C470 600 620 480 690 360 C750 250 720 110 620 70 C520 35 370 60 329 140 Z"
          fill="#ffffff" fill-opacity=".93" stroke="url(#heartStroke)" stroke-width="13" stroke-linejoin="round"/>

    <path d="M589 476 C565 425 490 425 485 485 C482 550 550 610 612 673 C670 610 725 540 712 475 C700 420 615 425 589 476 Z"
          fill="#fff" stroke="#fff" stroke-width="22" stroke-linejoin="round"/>
    <rect class="facilitator-photo" x="475" y="415" width="250" height="265" fill="url(#portraitFill)" clip-path="url(#portraitClip)" role="img" aria-label="Sepia portrait photo of the facilitator, Marisol Venhart"/>
    <path d="M589 476 C565 425 490 425 485 485 C482 550 550 610 612 673 C670 610 725 540 712 475 C700 420 615 425 589 476 Z"
          fill="none" stroke="#3fb34a" stroke-width="5" stroke-linejoin="round"/>
  </svg>

  <div class="title-block title-formula">
    MINDFULNESS <span class="plus">+</span> KINDNESS<br>
    <span class="plus">+</span> COMPASSIONATE COMMUNICATION <span class="plus">=</span>
  </div>
  <div class="title-block title-name">PALOMERE</div>
  <div class="title-block title-sub">COMMUNICATION</div>

  <div class="course-block course-label">CORE COURSE :</div>
  <div class="course-dates">11-12<br>DEC.</div>
  <div class="course-block course-venue">HARROW LANE CENTRE,<br>EDINBURGH</div>
  <div class="course-rule"></div>
  <div class="course-block course-price">£125/100</div>

  <section class="course-info">
    <p>Palomere Communication can help you<br>
      <strong>INCREASE AWARENESS &amp; COMPASSION<br>IN EVERYDAY SPEECH</strong> (with yourself &amp; others),<br>
      better understand your own patterns, and build<br>resilience to challenging situations.</p>
    <p>In this <strong>2-DAY CORE COURSE</strong>, we'll explore:</p>
    <ul>
      <li>Compassionate Communication;</li>
      <li>Buddhist Teachings on Right Speech, Loving-<span class="wrap">kindness, Right Effort, and more;</span></li>
      <li>Mindfulness Practices;</li>
      <li>Choices available to us in our everyday speech.</li>
    </ul>
    <p>This workshop will be of interest if you'd like to<br>
      improve personal and/or professional relationships.<br>
      Open to all, <strong>BEST SUITED TO THOSE<br>WITH AT LEAST 1 YEAR'S EXPERIENCE</strong> with<br>
      <strong>MINDFULNESS, BUDDHISM,</strong> or<br>
      <strong>COMPASSIONATE COMMUNICATION / NVC.</strong></p>
  </section>

  <div class="booking">
    <div class="booking-main">BOOKING ONLINE AT TICKETLOOM</div>
    <div class="booking-alt">or write <strong>marisol@palomere.co</strong></div>
  </div>

  <section class="facilitator">
    <div class="facilitator-label">FACILITATOR</div>
    <div class="facilitator-name">MARISOL VENHART</div>
    <p class="facilitator-bio">is an experienced group facilitator,<br>
      having worked with a range of organisations and<br>
      presented at a number of festivals &amp; conferences.<br>
      Marisol offers coaching in Palomere Communication.</p>
  </section>

  <div class="brand-mark"><span class="dot"></span><span class="name">Palomere</span></div>
  <div class="site-url">www.Palomere.co</div>
</main>
</body>
</html>
```